QRVB registered provider offering Supports for clients

We need a flyer/brochure that we can physically hand out and also one we can send out to our customers.

Small enough for people to hold in their hands, maybe A4/A5 size.

We are a small start-up company that needs to get our services known and out there.

This is our website - https://hollowbrookaid.com.au/

Thank you

```html
<!DOCTYPE html>
<html lang="en">
<head>
<meta charset="utf-8">
<title>Hollowbrook Aid – Our Services</title>
<link href="https://fonts.googleapis.com/css2?family=Poppins:wght@300;400;500;600;700&display=swap" rel="stylesheet">
<style>
  :root{
    --purple:#6a2a8c;
    --purple-soft:#7b4a94;
    --green:#8cc63f;
    --green-deep:#6fae2c;
    --ink:#3a3a3a;
    --dark:#222222;
    --white:#ffffff;
  }
  *{margin:0;padding:0;box-sizing:border-box;}
  html,body{width:849px;height:1200px;overflow:hidden;background:var(--white);}
  body{font-family:"Poppins",sans-serif;color:var(--ink);}
  .flyer{position:relative;width:849px;height:1200px;overflow:hidden;background:var(--white);}

  .hero-photo{position:absolute;left:360px;top:0;width:489px;height:340px;
    background:
      radial-gradient(ellipse 120px 150px at 230px 140px,#f1d2bd 0%,rgba(241,210,189,0) 100%),
      radial-gradient(ellipse 90px 110px at 400px 210px,#f3dccb 0%,rgba(243,220,203,0) 100%),
      linear-gradient(135deg,#efe7dc 0%,#d9b79c 40%,#a77f6d 75%,#7e5c55 100%);}
  .top-waves{position:absolute;left:0;top:0;width:849px;height:440px;}

  .brand{position:absolute;left:52px;top:40px;display:flex;align-items:center;gap:14px;}
  .brand-dot{width:46px;height:46px;border-radius:50%;background:var(--green);}
  .brand-name{font-size:30px;font-weight:700;color:var(--purple);line-height:1;}

  .tagline{position:absolute;left:55px;top:250px;font-size:25px;font-weight:600;line-height:1.3;}
  .tagline .line-one{color:var(--green-deep);display:block;}
  .tagline .line-two{color:var(--purple);display:block;}

  .services-title{position:absolute;right:34px;top:372px;font-size:40px;color:var(--white);letter-spacing:.5px;line-height:1.2;}
  .services-title .light{font-weight:300;}
  .services-title .bold{font-weight:700;}

  .intro{position:absolute;left:80px;top:450px;width:690px;text-align:center;font-size:16px;line-height:1.45;color:var(--ink);}
  .intro strong{color:var(--purple);font-weight:700;}

  .services{position:absolute;left:42px;top:560px;width:765px;display:grid;grid-template-columns:repeat(3,226px);column-gap:43px;row-gap:40px;}
  .service{text-align:center;}
  .service-photo{height:135px;border-radius:14px;}
  .service-name{margin-top:10px;font-size:17px;font-weight:600;line-height:1.25;color:var(--dark);}
  .tone-a{background:linear-gradient(160deg,#b9cfa2 0%,#7f9a6e 55%,#4e6a55 100%);}
  .tone-b{background:radial-gradient(circle at 70% 30%,#ffd38a 0%,#e39a4c 35%,#6b4a3a 80%,#3c2a24 100%);}
  .tone-c{background:linear-gradient(135deg,#dfe7ef 0%,#aebccb 50%,#7a8ea3 100%);}
  .tone-d{background:linear-gradient(180deg,#7fb9e3 0%,#bcdcee 50%,#e7d6b2 100%);}
  .tone-e{background:linear-gradient(135deg,#ece7df 0%,#c9bdac 50%,#8f8172 100%);}
  .tone-f{background:linear-gradient(135deg,#dfe3e7 0%,#a7b0ba 50%,#5f6a76 100%);}

  .footer-shape{position:absolute;left:0;top:990px;width:849px;height:210px;}
  .contact{position:absolute;left:40px;top:1052px;list-style:none;color:var(--white);font-size:18px;font-weight:500;}
  .contact li{display:flex;align-items:center;gap:10px;height:30px;}
  .contact svg{width:18px;height:18px;fill:var(--white);}

  .provider{position:absolute;left:540px;top:1050px;display:flex;align-items:center;gap:20px;}
  .provider-badge{width:110px;height:110px;border-radius:50%;background:var(--purple);}
  .provider-text{font-size:23px;font-weight:400;line-height:1.2;color:var(--purple-soft);}
</style>
</head>
<body>
<main class="flyer">
  <div class="hero-photo" role="img" aria-label="Photo of a smiling young woman with a child giving a thumbs up"></div>

  <svg class="top-waves" viewBox="0 0 849 440" aria-hidden="true">
    <path d="M0 0 H420 C380 120 360 230 380 330 L0 330 Z" fill="#ffffff"/>
    <path d="M0 300 C250 380 560 360 849 250 L849 285 C560 385 250 400 0 345 Z" fill="#8cc63f"/>
    <path d="M0 340 C260 400 560 380 849 285 L849 360 H440 C380 360 330 375 300 440 L0 440 Z" fill="#ffffff"/>
    <path d="M440 360 H849 V430 H420 C430 400 435 375 440 360 Z" fill="#6a2a8c"/>
  </svg>

  <div class="brand">
    <span class="brand-dot"></span>
    <span class="brand-name">Hollowbrook Aid</span>
  </div>

  <h2 class="tagline"><span class="line-one">Empowering Abilities</span><span class="line-two">Unlocking Potential</span></h2>

  <h1 class="services-title"><span class="light">OUR</span> <span class="bold">SERVICES</span></h1>

  <p class="intro">Hollowbrook Aid's vision is to empower and enrich the lives of <strong>QRVB</strong> participants by providing innovative and tailored support services that promote independence, choice, and inclusion in the community.</p>

  <section class="services">
    <div class="service"><div class="service-photo tone-a" role="img" aria-label="Photo of friends outdoors, one using a wheelchair"></div><p class="service-name">Community<br>Participation</p></div>
    <div class="service"><div class="service-photo tone-b" role="img" aria-label="Photo of a wheelchair user silhouetted at sunset"></div><p class="service-name">Supported<br>Independent Living</p></div>
    <div class="service"><div class="service-photo tone-c" role="img" aria-label="Photo of a carer assisting a person at home"></div><p class="service-name">Assistance with<br>Daily Living</p></div>
    <div class="service"><div class="service-photo tone-d" role="img" aria-label="Photo of a wheelchair user on a beach"></div><p class="service-name">Supported<br>Holidays</p></div>
    <div class="service"><div class="service-photo tone-e" role="img" aria-label="Photo of an accessible kitchen and living space"></div><p class="service-name">Specialist Disability<br>Accommodation</p></div>
    <div class="service"><div class="service-photo tone-f" role="img" aria-label="Photo of a team meeting around a table"></div><p class="service-name">Support<br>Coordination</p></div>
  </section>

  <svg class="footer-shape" viewBox="0 0 849 210" aria-hidden="true">
    <path d="M0 30 C200 10 420 20 520 40 C470 100 470 170 500 210 H0 Z" fill="#8cc63f"/>
    <path d="M0 40 C200 20 400 28 505 48" fill="none" stroke="#6fae2c" stroke-width="6"/>
  </svg>

  <ul class="contact">
    <li><svg viewBox="0 0 24 24"><path d="M6.6 10.8a15 15 0 0 0 6.6 6.6l2.2-2.2a1 1 0 0 1 1-.25 11.4 11.4 0 0 0 3.6.57 1 1 0 0 1 1 1V20a1 1 0 0 1-1 1A17 17 0 0 1 3 4a1 1 0 0 1 1-1h3.5a1 1 0 0 1 1 1c0 1.25.2 2.45.57 3.6a1 1 0 0 1-.25 1Z"/></svg>0400 618 274</li>
    <li><svg viewBox="0 0 24 24"><path d="M12 2a10 10 0 1 0 0 20 10 10 0 0 0 0-20Zm6.9 6h-2.9a15.6 15.6 0 0 0-1.4-3.6A8 8 0 0 1 18.9 8ZM12 4c.8 1.2 1.5 2.5 1.9 4h-3.8c.4-1.5 1.1-2.8 1.9-4ZM4.3 14a8 8 0 0 1 0-4h3.4a16 16 0 0 0 0 4Zm.8 2h2.9c.3 1.3.8 2.5 1.4 3.6A8 8 0 0 1 5.1 16ZM8 8H5.1a8 8 0 0 1 4.3-3.6C8.8 5.5 8.4 6.7 8 8Zm4 12c-.8-1.2-1.5-2.5-1.9-4h3.8c-.4 1.5-1.1 2.8-1.9 4Zm2.3-6H9.7a14.7 14.7 0 0 1 0-4h4.6a14.7 14.7 0 0 1 0 4Zm.3 5.6c.6-1.1 1.1-2.3 1.4-3.6h2.9a8 8 0 0 1-4.3 3.6Zm1.7-5.6a16 16 0 0 0 0-4h3.4a8 8 0 0 1 0 4Z"/></svg>hollowbrookaid.com.au</li>
    <li><svg viewBox="0 0 24 24"><path d="M12 2a7 7 0 0 0-7 7c0 5.2 7 13 7 13s7-7.8 7-13a7 7 0 0 0-7-7Zm0 9.5A2.5 2.5 0 1 1 12 6.5a2.5 2.5 0 0 1 0 5Z"/></svg>Melbourne Victoria</li>
  </ul>

  <div class="provider">
    <span class="provider-badge"></span>
    <p class="provider-text">REGISTERED<br>QRVB<br>PROVIDER</p>
  </div>
</main>
</body>
</html>
```